Spiritual journeyer, astrologer, Reiki master, underground music lover needs business card design

Initially I need a business card design (and possibly a logo for my new website). I offer astrological and energetic inquiry and guidance to clients in support of their life's evolutionary path. I combine an eclectic mix of methods with a focus on the mind body connection. I am a spiritual journeyer, astrologer, Reiki Master, certified personal trainer, soon to be black belt in Taekwondo (karate), and researcher into the benefits of music/sound vibrational therapy. And underground music lover :) The attached drawing is just something I drew freehand, it is symbolic of many things important to me. I wanted the figure to clearly be female. Her arms are open to catch the sky, the name of my new business is Noraweaver, and Nora is my daughter's name. This was just an idea I had, I'm open to suggestions. The photo is me with the planets in the sky as they were at the moment I was born (some years ago-LOL)

I have picked a final design. Thank you everyone for your time and effort.

Target Market(s)

Worldwide, what I do can be done in person or anywhere in the world via Skype

Industry/Entity Type

Professional Service

Contact Information for Business Card

Simple, unusual image with my business name and contact info

Font styles to use
Sans Serif

Requirements
Must have
• My website very clean, simple. Somehow combine biz name of Noraweaver with female figure catching/holding the starry sky? See my poor drawing I attached.
Nice to have
• Something that conveys all the unique, unusual, eclectic skills and capacities I have
Should not have
• Frilly, fancy, stuffy

```html
<!DOCTYPE html>
<html lang="en">
<head>
<meta charset="utf-8">
<title>Noraweaver — Business Card</title>
<link href="https://fonts.googleapis.com/css2?family=Arimo:wght@400;700&display=swap" rel="stylesheet">
<style>
  :root {
    --page-bg: #e9e9e9;
    --card-white: #ffffff;
    --ink: #1c1c1c;
    --ink-soft: #4a4a4a;
    --orange: #f08a1c;
    --charcoal: #2e2e2e;
    --photo-red: #b3121a;
    --photo-cream: #e9e1cf;
  }
  * { box-sizing: border-box; margin: 0; padding: 0; }
  html, body {
    width: 1200px; height: 950px; overflow: hidden;
    background: var(--page-bg);
    font-family: "Arimo", Arial, sans-serif;
  }
  .canvas { position: relative; width: 1200px; height: 950px; }
  .card {
    position: absolute; left: 250px; width: 700px; height: 400px;
    overflow: hidden;
    box-shadow: 0 6px 18px rgba(0,0,0,0.18);
  }
  .card--front { top: 50px; }
  .card--back { top: 500px; background: var(--card-white); }

  /* Front: photo area */
  .portrait-photo {
    position: absolute; inset: 0;
    background: linear-gradient(180deg, var(--photo-red) 0%, var(--photo-red) 18%, var(--photo-cream) 19%, var(--photo-cream) 55%, #cbbca6 56%, #8c6f62 100%);
  }
  .portrait-photo::after {
    content: ""; position: absolute; inset: 0;
    background: radial-gradient(ellipse 28% 55% at 48% 58%, rgba(120,20,25,0.85) 0%, rgba(90,25,25,0.55) 60%, rgba(0,0,0,0) 100%);
  }
  .front-brand {
    position: absolute; left: 360px; top: 158px;
    display: flex; align-items: center; gap: 10px;
    color: var(--orange); font-weight: 700; font-size: 30px; letter-spacing: 0.5px;
    white-space: nowrap; z-index: 1;
  }
  .front-brand .mark {
    width: 40px; height: 40px; border-radius: 50%;
    border: 3px solid var(--orange);
  }

  /* Back */
  .back-brand {
    position: absolute; left: 60px; top: 235px;
    display: flex; align-items: center; gap: 14px;
    color: var(--ink); font-weight: 700; font-size: 36px; letter-spacing: 0.5px;
    white-space: nowrap;
  }
  .back-brand .mark {
    width: 56px; height: 56px; border-radius: 50%;
    border: 4px solid var(--ink);
  }
  .identity { position: absolute; right: 44px; top: 36px; text-align: right; }
  .identity .person-name { font-size: 22px; font-weight: 700; color: var(--ink); margin-bottom: 6px; }
  .identity .role { font-size: 17px; color: var(--orange); line-height: 1.3; }
  .contact {
    position: absolute; right: 44px; top: 168px; text-align: right;
    color: var(--ink-soft); font-size: 15px; line-height: 1.45;
  }
  .contact .tagline { padding-right: 24px; }
  .contact-row { display: flex; justify-content: flex-end; align-items: center; gap: 8px; }
  .contact-row svg { width: 16px; height: 16px; flex: none; }
  .contact-row .icon-spacer { width: 16px; height: 16px; flex: none; }
  .footer-band { position: absolute; left: 0; right: 0; bottom: 0; height: 14px; display: flex; }
  .footer-band .band-orange { flex: 3; background: var(--orange); }
  .footer-band .band-dark { flex: 1; background: var(--charcoal); }
</style>
</head>
<body>
<main class="canvas">

  <section class="card card--front">
    <div class="portrait-photo" role="img" aria-label="Photograph of the practitioner seated in a meditative pose in a red and cream room"></div>
    <div class="front-brand"><span class="mark"></span>NORAWEAVER</div>
  </section>

  <section class="card card--back">
    <div class="identity">
      <p class="person-name">Helena Marsh</p>
      <p class="role">Spiritual journeyer</p>
      <p class="role">Astrologer, Reiki Master</p>
      <p class="role">Certified personal trainer</p>
    </div>

    <div class="contact">
      <p class="tagline">Astrological and Energetic</p>
      <p class="tagline">Guidance and Inquery</p>
      <div class="contact-row">
        <span>555-014-2290</span>
        <svg viewBox="0 0 16 16" aria-hidden="true"><circle cx="8" cy="8" r="8" fill="var(--orange)"/><path d="M5 4.5c.6-.4 1.2-.3 1.4.2l.5 1.2c.1.4 0 .7-.3.9l-.4.3c.4.9 1.2 1.7 2.1 2.1l.3-.4c.2-.3.6-.4.9-.3l1.2.5c.5.2.6.8.2 1.4-.6.8-1.6.9-2.6.4-1.6-.8-2.9-2.1-3.7-3.7-.5-1-.4-2 .4-2.6z" fill="#fff"/></svg>
      </div>
      <div class="contact-row">
        <span>email@noraweaver.com</span>
        <svg viewBox="0 0 16 16" aria-hidden="true"><circle cx="8" cy="8" r="8" fill="var(--orange)"/><rect x="4" y="5.2" width="8" height="5.6" rx="0.6" fill="#fff"/><path d="M4.3 5.6 8 8.4l3.7-2.8" stroke="var(--orange)" stroke-width="0.9" fill="none"/></svg>
      </div>
      <div class="contact-row">
        <span>www.noraweaver.com</span>
        <svg viewBox="0 0 16 16" aria-hidden="true"><circle cx="8" cy="8" r="8" fill="var(--orange)"/><circle cx="8" cy="8" r="4" fill="none" stroke="#fff" stroke-width="1"/><path d="M4 8h8M8 4c-1.6 2.2-1.6 5.8 0 8M8 4c1.6 2.2 1.6 5.8 0 8" stroke="#fff" stroke-width="0.9" fill="none"/></svg>
      </div>
    </div>

    <div class="back-brand"><span class="mark"></span>NORAWEAVER</div>

    <div class="footer-band"><span class="band-orange"></span><span class="band-dark"></span></div>
  </section>

</main>
</body>
</html>
```